Home Page Design for Motor Manufacturer

Hello,
please design the homepage for a manufacturer of industry motors. I am looking for a professional, clean and minimalistic design. Since this a rather conservative industry it should get a professional look but since it is a redesign there should be some modern that gives is the modern touch of innovation.
A competitor's homepage I like is:
https://www.valtrosen.com/en/
What I like about this website:
* clean, minimal, well structured design
* mega menu
For this project please find attached the wireframes (most buttons are in German but by context and Google translate you will easily figure it out; only unclear - "Messe" means "trade exhibition"). The paddings and margins are NOT exact. Also any color of backgrounds etc. chosen is not meant to represent a real color but rather to illustrate the object and maybe show there should be some background emphasis (color or image).
Wireframes:
https: //www.filquarry. com / t / pWmeTuZa8LkiBvQx
In both wireframes the only thing that is different is the Service section. I expect from the winner both designs for this service section: one with normal cart design and one with tabs as filters to search products (find image for product categories attached)
In the header use on the left the following text:
h1: "Your competent partner for industrial engines,
-transmission and drawing parts
with more than 5000 satisfied customers "
primary button: Our products
sec. button: Download catalog
and on the right side we feature one or more product images (like putting them in a nice display together).
I also think of a solid background color or subtle gradient for the hero section.
The winner should also design an open mega menu version.
Menu items in this order:
• Home page
• Gearboxes & Motors
• Engine components
• Drawing parts
• Machines & accessories
• About us
• Contact
Also create a language switch with globe symbol and DE for Germany and EN for English above the nav plus the telephone number with icon (user dummy number +49 (0) 987650432)
Output should be in Figma, Sketch or PSD.
Fonts + color to use:
header: Proza Libre, bold, # 0171A1
body: Open Sans, regular, black
Primary accent color: # 0171A1
Text black or dark gray
background: light gray, white or shade of blue
More image resources:
https://www.filquarry.com/t/RnaHwoqPEdLu5sjv
If there are any questions please do not hesitate to ask.
Target Market(s)
B2B - anyone with industrial machinery needing small motors (not car engines)
Industry/Entity Type
Manufacturing
Number of Pages Required
1 page
Requirements
Must have
- see above
Nice to have
- see above
Should not have
- see above

```html
<!DOCTYPE html>
<html lang="en">
<head>
<meta charset="utf-8">
<title>Orvek GmbH – Industrial Motors, Transmissions and Drawing Parts</title>
<link rel="stylesheet" href="https://fonts.googleapis.com/css2?family=Open+Sans:ital,wght@0,400;0,600;0,700;1,400&family=Proza+Libre:wght@600;700;800&display=swap">
<style>
:root{
  --accent:#0171a1;
  --accent-dark:#0d4f7e;
  --cyan-1:#4dc1e8;
  --cyan-2:#1aa7cf;
  --blue-3:#0a78a8;
  --ink:#222;
  --text:#6b6b6b;
  --muted:#9a9a9a;
  --line:#e3e3e3;
  --panel:#f6f6f6;
  --white:#fff;
}
*{box-sizing:border-box;margin:0;padding:0}
html,body{width:1200px;height:5000px;overflow:hidden;background:var(--white)}
body{position:relative;font-family:"Open Sans",sans-serif;color:var(--text);font-size:12px}
.abs{position:absolute}
h2.section-title{position:absolute;left:0;width:1200px;text-align:center;font-family:"Proza Libre",sans-serif;font-weight:700;font-size:27px;color:var(--ink);letter-spacing:.5px}
.btn{position:absolute;display:flex;align-items:center;justify-content:center;font-family:"Open Sans",sans-serif;font-weight:700;font-size:10px;letter-spacing:.3px;text-transform:uppercase}
.btn-solid{background:var(--accent);color:var(--white)}
.btn-outline{border:2px solid var(--accent);color:var(--accent);background:var(--white)}

/* header */
.top-bar{left:0;top:0;width:1200px;height:9px;background:var(--accent)}
.brand{left:161px;top:22px;display:flex;align-items:center;gap:8px;font-family:"Proza Libre",sans-serif;font-weight:800;font-size:30px;color:var(--accent);letter-spacing:1px}
.brand-dot{width:12px;height:12px;background:var(--accent);border-radius:50%}
.search{left:407px;top:25px;width:315px;height:32px;border:1px solid var(--line);border-radius:2px;display:flex;align-items:center;justify-content:space-between;padding:0 12px;font-size:10px;color:#b5b5b5}
.util{top:32px;display:flex;align-items:center;gap:6px;font-size:10px;color:var(--accent)}
.nav{left:0;top:72px;width:1200px;height:60px;border-top:1px solid var(--line);border-bottom:1px solid var(--line)}
.nav ul{list-style:none;position:absolute;left:161px;width:878px;top:0;height:58px;display:flex;justify-content:space-between;align-items:center}
.nav li{font-size:11px;color:#444;text-transform:uppercase;letter-spacing:.3px}

/* hero */
.hero{left:0;top:132px;width:1200px;height:753px;background:linear-gradient(100deg,#dcdee0 0%,#ececed 40%,#f7f7f7 75%,#fafafa 100%);overflow:hidden}
.hero-eyebrow{left:161px;top:320px;font-size:9.5px;letter-spacing:2px;color:var(--accent);text-transform:uppercase}
.hero-title{left:161px;top:338px;width:460px;font-family:"Proza Libre",sans-serif;font-weight:700;font-size:25px;line-height:38px;color:var(--accent);white-space:nowrap}
.hero-title u{text-decoration-thickness:2px}
.hero-visual{left:689px;top:262px;width:437px;height:360px;border-radius:50% 40% 45% 50%;background:radial-gradient(circle at 60% 40%,#c6cbcf 0%,#dde0e2 45%,rgba(240,240,240,0) 72%)}
.dots{left:573px;top:728px;display:flex;gap:8px;align-items:center}
.dots span{width:9px;height:9px;border-radius:50%;background:#bcd7e4}
.dots .on{width:18px;height:18px;border:2px solid var(--accent);background:radial-gradient(circle,var(--accent) 0 4px,transparent 5px)}

.perks{left:161px;top:771px;width:878px;height:224px;display:flex}
.perk{flex:1;color:var(--white);text-align:center;padding-top:56px}
.perk h3{font-family:"Proza Libre",sans-serif;font-size:13px;font-weight:700}
.perk hr{width:22px;border:0;border-top:1px solid rgba(255,255,255,.8);margin:12px auto 14px}
.perk p{font-size:10.5px;line-height:22px;width:160px;margin:0 auto}

/* products */
.tabs{left:408px;top:1128px;display:flex;gap:5px}
.tab{width:91px;height:90px;background:#ededed;display:flex;flex-direction:column;align-items:center;justify-content:center;gap:8px;font-size:9.5px;color:var(--accent)}
.tab.active{background:var(--accent);color:var(--white)}
.subfilter{left:0;top:1254px;width:1200px;display:flex;justify-content:center;font-size:10px;color:#555;text-transform:uppercase}
.subfilter span{padding:0 18px;border-left:1px solid var(--line)}
.subfilter span:first-child{border-left:0}
.card{width:278px;height:278px;border:1px solid var(--line);background:var(--white)}
.card-photo{position:absolute;left:69px;top:50px;width:140px;height:120px;border-radius:40%;background:radial-gradient(circle,#9aa3aa 0%,#c9ced2 45%,rgba(255,255,255,0) 72%)}
.card-title{position:absolute;left:0;width:100%;top:196px;text-align:center;font-size:11.5px;font-weight:600;color:#444}

/* trade fairs */
.fairs{left:0;top:2186px;width:1200px;height:1174px;background:var(--panel);border-top:1px solid var(--line);border-bottom:1px solid var(--line)}
.fair-photo{left:161px;width:353px;height:272px;background:linear-gradient(135deg,#3d74b8 0%,#5b8fd0 50%,#7aa6dc 100%)}
.fair-title{left:559px;font-family:"Proza Libre",sans-serif;font-weight:600;font-size:15px;color:#333}
.fair-text{left:559px;width:470px;font-size:10.5px;line-height:22.5px;color:var(--text)}
.fair-rule{left:161px;width:878px;height:1px;background:var(--line)}

/* about */
.team-photo{background:linear-gradient(160deg,#9fb3cc 0%,#cdd7e4 55%,#e9edf2 100%)}
.about-text{left:678px;width:355px;font-size:10.5px;line-height:22.5px}
.about-list{left:678px;list-style:none}
.about-list li{font-size:10.5px;font-weight:600;color:#333;line-height:26.5px;display:flex;align-items:center;gap:10px}
.about-list li::before{content:"";width:5px;height:5px;border-radius:50%;background:var(--accent)}
.learn{left:678px;top:3830px;font-size:10.5px;font-weight:700;color:var(--accent);display:flex;align-items:center;gap:6px;text-transform:uppercase}

/* downloads */
.downloads{left:0;top:3917px;width:1200px;height:556px;background:var(--panel);border-top:1px solid var(--line)}
.dl-card{left:161px;top:4072px;width:878px;height:323px;background:var(--white);border:1px solid var(--line)}
.dl-photo{left:161px;top:4072px;width:336px;height:323px;background:linear-gradient(135deg,#7f8d9c 0%,#b6c0ca 45%,#dfe4e8 100%)}
.dl-text{left:542px;width:460px;font-size:10.5px;line-height:22.5px}

/* contact strip */
.contact-strip{left:161px;top:4540px;width:878px;display:flex;justify-content:space-between}
.contact-strip div{font-size:10.5px;color:#666;line-height:20px}
.contact-strip strong{display:block;font-size:12.5px;color:#222;font-weight:600}

/* footer */
.footer{left:0;top:4657px;width:1200px;height:343px;background:var(--accent);color:var(--white)}
.footer h4{position:absolute;top:62px;font-family:"Proza Libre",sans-serif;font-size:17px;font-weight:600}
.footer p,.footer ul{position:absolute;top:108px;font-size:10px;line-height:22px}
.footer ul{list-style:none}
.footer li::before{content:"» "}
.newsletter{position:absolute;left:835px;top:169px;width:204px;height:35px;background:#fff;display:flex;align-items:center}
.newsletter span{flex:1;height:100%;background:#1b84b0;display:flex;align-items:center;padding-left:14px;font-size:9.5px}
.newsletter i{width:37px;display:flex;justify-content:center}
.footer-bottom{position:absolute;top:270px;left:161px;width:878px;display:flex;justify-content:space-between;align-items:center;font-size:10px}
.social{display:flex;gap:9px;align-items:center}
.social span{width:9px;height:9px;border-radius:50%;background:#fff}
</style>
</head>
<body>

<header>
  <div class="abs top-bar"></div>
  <div class="abs brand"><span class="brand-dot"></span>Orvek</div>
  <div class="abs search">Make your search here...
    <svg width="12" height="12" viewBox="0 0 12 12"><circle cx="5" cy="5" r="3.8" fill="none" stroke="#c5c5c5" stroke-width="1.3"/><path d="M8 8l3 3" stroke="#c5c5c5" stroke-width="1.3"/></svg>
  </div>
  <div class="abs util" style="left:865px">
    <svg width="11" height="11" viewBox="0 0 24 24"><path fill="#0171a1" d="M6.6 10.8a15 15 0 0 0 6.6 6.6l2.2-2.2c.3-.3.7-.4 1-.2 1.1.4 2.3.6 3.6.6.6 0 1 .4 1 1V20c0 .6-.4 1-1 1A17 17 0 0 1 3 4c0-.6.4-1 1-1h3.5c.6 0 1 .4 1 1 0 1.3.2 2.5.6 3.6.1.3 0 .7-.2 1z"/></svg>
    +49 (0) 987650432
  </div>
  <div class="abs util" style="left:995px">
    <svg width="11" height="11" viewBox="0 0 12 12" fill="none" stroke="#0171a1" stroke-width="1"><circle cx="6" cy="6" r="5"/><ellipse cx="6" cy="6" rx="2.2" ry="5"/><path d="M1 6h10"/></svg>
    DE ▾
  </div>
  <nav class="abs nav">
    <ul>
      <li>Home</li><li>Gearbox &amp; Motors</li><li>Engine Components</li><li>Drawing Parts</li><li>Machines &amp; Accessories</li><li>About Us</li><li>Contact</li>
    </ul>
  </nav>
</header>

<section>
  <div class="abs hero">
    <svg class="abs" style="left:0;top:0" width="1200" height="753" viewBox="0 0 1200 753" fill="none" stroke="#ffffff" stroke-opacity=".55" stroke-width="1.2">
      <path d="M380 0 C520 200 700 320 1200 360"/>
      <path d="M440 0 C580 170 760 280 1200 300"/>
      <path d="M0 560 C300 560 600 640 900 753"/>
    </svg>
  </div>
  <div class="abs hero-eyebrow">Welcome to Orvek GmbH</div>
  <h1 class="abs hero-title">Your competent partner for the<br>industrial engines - transmission<br>and drawing parts with more than<br><u>5000</u> satisfied costumers!</h1>
  <div class="btn btn-solid" style="left:161px;top:526px;width:138px;height:45px">Our Products</div>
  <div class="btn btn-outline" style="left:311px;top:526px;width:174px;height:45px">Download Catalog</div>
  <div class="abs hero-visual" role="img" aria-label="Arrangement of a planetary gearbox, an angle gearbox and a geared motor"></div>
  <div class="abs dots"><span></span><span class="on"></span><span></span></div>

  <div class="abs perks">
    <div class="perk" style="background:var(--cyan-1)"><h3>Vorteil 1</h3><hr><p>Lorem Ipsum is simply dummy text of the printing and typesetting industry.</p></div>
    <div class="perk" style="background:var(--cyan-2)"><h3>Vorteil 2</h3><hr><p>Lorem Ipsum is simply dummy text of the printing and typesetting industry.</p></div>
    <div class="perk" style="background:var(--blue-3)"><h3>Vorteil 3</h3><hr><p>Lorem Ipsum is simply dummy text of the printing and typesetting industry.</p></div>
    <div class="perk" style="background:var(--accent-dark)"><h3>Vorteil 3</h3><hr><p>Lorem Ipsum is simply dummy text of the printing and typesetting industry.</p></div>
  </div>
</section>

<section>
  <h2 class="section-title" style="top:1064px">PRODUKTE</h2>
  <div class="abs tabs">
    <div class="tab active"><svg width="26" height="22" viewBox="0 0 26 22" fill="none" stroke="#fff" stroke-width="1.3"><rect x="3" y="6" width="14" height="11"/><rect x="17" y="8" width="6" height="7"/><path d="M6 6V3h8v3"/></svg>Kategorie 1</div>
    <div class="tab"><svg width="24" height="24" viewBox="0 0 24 24" fill="none" stroke="#0171a1" stroke-width="1.2"><circle cx="12" cy="12" r="10"/><circle cx="12" cy="12" r="5"/><circle cx="12" cy="12" r="1.5"/></svg>Kategorie 2</div>
    <div class="tab"><svg width="24" height="24" viewBox="0 0 24 24" fill="none" stroke="#0171a1" stroke-width="1.2"><circle cx="12" cy="12" r="7" stroke-dasharray="3 2"/><circle cx="12" cy="12" r="3"/></svg>Kategorie 1</div>
    <div class="tab"><svg width="28" height="20" viewBox="0 0 28 20" fill="none" stroke="#0171a1" stroke-width="1.2"><rect x="6" y="4" width="14" height="12"/><path d="M2 10h4M20 10h6M10 4v12M14 4v12"/></svg>Kategorie 4</div>
  </div>
  <div class="abs subfilter"><span>Alle</span><span>Unterkategorie 1</span><span>Unterkategorie 2</span></div>

  <div class="abs card" style="left:161px;top:1330px"><div class="card-photo" role="img" aria-label="Geared motor product photo"></div><div class="card-title">Product Category Title Goes Here</div></div>
  <div class="abs card" style="left:461px;top:1330px"><div class="card-photo" role="img" aria-label="Angle gearbox product photo"></div><div class="card-title">Product Category Title Goes Here</div></div>
  <div class="abs card" style="left:761px;top:1330px"><div class="card-photo" role="img" aria-label="Planetary gear motor product photo"></div><div class="card-title">Product Category Title Goes Here</div></div>
  <div class="btn btn-solid" style="left:230px;top:1654px;width:140px;height:43px">See Details</div>
  <div class="btn btn-solid" style="left:530px;top:1654px;width:140px;height:43px">See Details</div>
  <div class="btn btn-solid" style="left:830px;top:1654px;width:140px;height:43px">See Details</div>

  <div class="abs card" style="left:161px;top:1744px"><div class="card-photo" role="img" aria-label="DC motor product photo"></div><div class="card-title">Product Category Title Goes Here</div></div>
  <div class="abs card" style="left:461px;top:1744px"><div class="card-photo" role="img" aria-label="Cycloidal reducer product photo"></div><div class="card-title">Product Category Title Goes Here</div></div>
  <div class="abs card" style="left:761px;top:1744px"><div class="card-photo" role="img" aria-label="Planetary gear motor product photo"></div><div class="card-title">Product Category Title Goes Here</div></div>
  <div class="btn btn-solid" style="left:230px;top:2068px;width:140px;height:43px">See Details</div>
  <div class="btn btn-solid" style="left:530px;top:2068px;width:140px;height:43px">See Details</div>
  <div class="btn btn-solid" style="left:830px;top:2068px;width:140px;height:43px">See Details</div>
</section>

<section>
  <div class="abs fairs"></div>
  <h2 class="section-title" style="top:2254px">MESSEN</h2>

  <div class="abs fair-photo" style="top:2348px" role="img" aria-label="Motor components displayed on a blue exhibition table"></div>
  <div class="abs fair-title" style="top:2344px">Titel Messen</div>
  <p class="abs fair-text" style="top:2375px">Lorem Ipsum is simply dummy text of the printing and typesetting industry. Lorem Ipsum has been the industry's standard dummy text ever since the 1500s, when an unknown printer took a galley of type and scrambled it to make a type specimen book. It has now survived not only five centuries, but also the leap into electronic typesetting, remaining essentially unchanged. It was popularised in the 1960s with the release of Typemark sheets containing Lorem Ipsum passages, and more recently with desktop publishing software like Quillset Layout including versions of Lorem Ipsum</p>
  <div class="btn btn-solid" style="left:716px;top:2575px;width:171px;height:43px">Kostenloses Ticket</div>
  <div class="btn btn-outline" style="left:899px;top:2575px;width:128px;height:43px">View Details</div>
  <div class="abs fair-rule" style="top:2650px"></div>

  <div class="abs fair-photo" style="top:2680px" role="img" aria-label="Stamped stator laminations on a blue exhibition table"></div>
  <div class="abs fair-title" style="top:2676px">Titel Messen</div>
  <p class="abs fair-text" style="top:2707px">Lorem Ipsum is simply dummy text of the printing and typesetting industry. Lorem Ipsum has been the industry's standard dummy text ever since the 1500s, when an unknown printer took a galley of type and scrambled it to make a type specimen book. It has now survived not only five centuries, but also the leap into electronic typesetting, remaining essentially unchanged. It was popularised in the 1960s with the release of Typemark sheets containing Lorem Ipsum passages, and more recently with desktop publishing software like Quillset Layout including versions of Lorem Ipsum</p>
  <div class="btn btn-solid" style="left:716px;top:2907px;width:171px;height:43px">Kostenloses Ticket</div>
  <div class="btn btn-outline" style="left:899px;top:2907px;width:128px;height:43px">View Details</div>
  <div class="abs fair-rule" style="top:2982px"></div>

  <div class="abs fair-photo" style="top:3012px" role="img" aria-label="Drawn metal parts on a blue exhibition table"></div>
  <div class="abs fair-title" style="top:3008px">Titel Messen</div>
  <p class="abs fair-text" style="top:3039px">Lorem Ipsum is simply dummy text of the printing and typesetting industry. Lorem Ipsum has been the industry's standard dummy text ever since the 1500s, when an unknown printer took a galley of type and scrambled it to make a type specimen book. It has now survived not only five centuries, but also the leap into electronic typesetting, remaining essentially unchanged. It was popularised in the 1960s with the release of Typemark sheets containing Lorem Ipsum passages, and more recently with desktop publishing software like Quillset Layout including versions of Lorem Ipsum</p>
  <div class="btn btn-solid" style="left:716px;top:3239px;width:171px;height:43px">Kostenloses Ticket</div>
  <div class="btn btn-outline" style="left:899px;top:3239px;width:128px;height:43px">View Details</div>
</section>

<section>
  <h2 class="section-title" style="top:3427px">UBER UNS</h2>
  <div class="abs team-photo" style="left:161px;top:3511px;width:278px;height:204px" role="img" aria-label="Company team at a trade fair booth"></div>
  <div class="abs team-photo" style="left:351px;top:3651px;width:262px;height:194px;border:4px solid #fff" role="img" aria-label="Team group at the exhibition stand"></div>
  <p class="abs about-text" style="top:3505px">Contrary to popular belief, Lorem Ipsum is not simply random text. It has roots in a piece of classical Latin literature from 45 BC, making it over 2000 years old. Martin Halvard, a Latin professor at Brackwell College in Ostmark, looked up one of the more obscure Latin words, consectetur, from a Lorem Ipsum.</p>
  <ul class="abs about-list" style="top:3627px">
    <li>Feature Example Number One Goes Here</li>
    <li>Feature Example Number Two Goes Here</li>
    <li>Feature Example Number Three Goes Here</li>
  </ul>
  <p class="abs about-text" style="top:3719px">(The Extremes of Good and Evil) by Varenus, written in 45 BC. This book is a treatise on the theory of ethics, very popular during the Renaissance. The first line of Lorem Ipsum, "Lorem ipsum dolor sit amet, comes from a line in section 1.10.32.</p>
  <div class="abs learn">Learn More <svg width="16" height="8" viewBox="0 0 16 8"><path d="M0 4h14M11 1l3 3-3 3" fill="none" stroke="#0171a1" stroke-width="1.2"/></svg></div>
</section>

<section>
  <div class="abs downloads"></div>
  <h2 class="section-title" style="top:3984px">DOWNLOADS</h2>
  <div class="abs dl-card"></div>
  <div class="abs dl-photo" role="img" aria-label="Close-up of gear components and reducer parts"></div>
  <div class="abs dots" style="left:302px;top:4364px"><span style="background:#d7dde2"></span><span class="on" style="border-color:#fff;background:radial-gradient(circle,#fff 0 4px,transparent 5px)"></span><span style="background:#d7dde2"></span></div>
  <p class="abs dl-text" style="top:4104px">Lorem Ipsum is simply dummy text of the printing and typesetting industry. Lorem Ipsum has been the industry's <b><i>standard dummy text ever since the 1500s</i></b>, right when an unknown printer took a galley of type and scrambled it to make a type specimen book. It has now survived not only five centuries, but also the leap into electronic typesetting, remaining essentially unchanged.</p>
  <p class="abs dl-text" style="top:4232px">Lorem Ipsum passages, and more recently with desktop publishing software like Quillset Layout including versions of Lorem Ipsum.</p>
  <div class="btn btn-solid" style="left:542px;top:4305px;width:128px;height:45px">Download</div>
</section>

<section class="abs contact-strip">
  <div>Request your quote, call us now!<strong>+49 (0) 987650432</strong></div>
  <div style="margin-left:60px">Write your enquiry<strong>email@example.com</strong></div>
  <div style="text-align:right">Do you have any specific request?<strong>Get in touch with us</strong></div>
</section>

<footer class="abs footer">
  <h4 style="left:161px">About Company</h4>
  <p style="left:161px;width:215px">Lorem Ipsum is simply dummy text of the printing and typesetting industry. It has been the industry's standard dummy text ever since the late 1500's</p>
  <h4 style="left:449px">Quick Links</h4>
  <ul style="left:449px"><li>Sitemap</li><li>Privacy Policy</li><li>Imprint</li><li>Terms &amp; Conditions</li><li>Delivery</li></ul>
  <h4 style="left:643px">Solutions</h4>
  <ul style="left:643px"><li>Lorem Ipsum</li><li>Simply Dumm Text</li><li>Dolor Amet Post</li><li>Lorem &amp; Valaherist</li><li>Ipsum Standards</li></ul>
  <h4 style="left:835px">Newsletter</h4>
  <p style="left:835px;width:210px">Subscribe below to get notified with all the news and updates from us</p>
  <div class="newsletter"><span>Your E-mail Address</span><i><svg width="14" height="14" viewBox="0 0 14 14"><path d="M1 6.5L13 1 9 13 7 8z" fill="#0171a1"/></svg></i></div>
  <div class="footer-bottom">
    <div><b>Copyright 2020 © Orvek</b> - All Rights Reserved</div>
    <div class="social">Find Us At: <span></span><span></span><span></span></div>
  </div>
</footer>

</body>
</html>
```